VELKORIS Stationery Design Project

I want a stationery design for a web development company consists of:
1- business card
2- Letter Head
3- small Envelope
4- Large Envelope

need a very clean professional simple design yet creative,

The company logo is attached
http://www.pixelbazaarhub.net/project-progress/designs.aspx?briefId=5830174&submissionId=47210938

logo font is sui generis rg (attached)
I would like to have the stationery text font to be helvetica font regular or light (can be changed)

I love the combination of cyan, black and grey colors
( will attach some recommended styles)

Business

• curves or waves

```html
<!DOCTYPE html>
<html lang="en">
<head>
<meta charset="UTF-8">
<title>VELKORIS Business Card</title>
<link href="https://fonts.googleapis.com/css2?family=Open+Sans:wght@400;600&family=Saira:wght@500&display=swap" rel="stylesheet">
<style>
  :root {
    --canvas-bg: #ecebea;
    --card-dark: #1a1a1b;
    --card-dark-mark: #3a3a3c;
    --card-light: #ffffff;
    --cyan: #1e9fe0;
    --grey: #8a8c90;
    --ink: #2b2b2d;
  }
  * { margin: 0; padding: 0; box-sizing: border-box; }
  html, body { width: 1200px; height: 1200px; overflow: hidden; }
  body {
    background: var(--canvas-bg);
    font-family: "Open Sans", Arial, sans-serif;
    position: relative;
  }
  .card {
    position: absolute;
    left: 270px;
    width: 660px;
    height: 378px;
    box-shadow: 0 6px 18px rgba(0,0,0,0.18);
  }
  .card-back {
    top: 150px;
    background: var(--card-dark);
    display: flex;
    align-items: center;
    justify-content: center;
  }
  .card-back .back-name {
    font-weight: 600;
    font-size: 64px;
    letter-spacing: 10px;
    color: var(--card-dark-mark);
  }
  .card-front {
    top: 672px;
    background: var(--card-light);
  }
  .brand {
    position: absolute;
    left: 48px;
    top: 56px;
    display: flex;
    align-items: center;
    gap: 12px;
  }
  .brand-square {
    width: 22px;
    height: 22px;
    background: var(--cyan);
  }
  .brand-name {
    font-weight: 600;
    font-size: 28px;
    letter-spacing: 6px;
    color: var(--cyan);
  }
  .holder {
    position: absolute;
    left: 48px;
    top: 170px;
  }
  .holder-name {
    font-family: "Saira", "Open Sans", sans-serif;
    font-weight: 500;
    font-size: 26px;
    color: var(--cyan);
    line-height: 1.1;
  }
  .holder-role {
    font-size: 15px;
    color: var(--ink);
    margin-top: 2px;
  }
  .contact {
    position: absolute;
    left: 390px;
    top: 230px;
    font-size: 16px;
    color: var(--ink);
    line-height: 1.35;
    list-style: none;
  }
  .contact .address { margin-bottom: 6px; }
  .contact li { display: flex; align-items: center; gap: 8px; }
  .contact svg { width: 13px; height: 13px; flex: none; fill: var(--cyan); }
</style>
</head>
<body>
  <section class="card card-back" aria-label="Card back">
    <span class="back-name">VELKORIS</span>
  </section>

  <section class="card card-front" aria-label="Card front">
    <div class="brand">
      <span class="brand-square"></span>
      <span class="brand-name">VELKORIS</span>
    </div>

    <div class="holder">
      <p class="holder-name">Arlen Doyce</p>
      <p class="holder-role">President</p>
    </div>

    <ul class="contact">
      <li class="address">55 demo street, demo place<br>P.O. Box 000, 555 Avenue</li>
      <li>
        <svg viewBox="0 0 16 16" aria-hidden="true"><path d="M3 1h3l1.5 4-2 1.2a9 9 0 0 0 4.3 4.3L11 8.5l4 1.5v3a2 2 0 0 1-2 2A13 13 0 0 1 1 3a2 2 0 0 1 2-2z"/></svg>
        888-8888-8888
      </li>
      <li>
        <svg viewBox="0 0 16 16" aria-hidden="true"><path d="M1 3h14v10H1z M1 3l7 6 7-6" stroke="#fff" stroke-width="1"/></svg>
        info@websitename.com
      </li>
      <li>
        <svg viewBox="0 0 16 16" aria-hidden="true"><circle cx="8" cy="8" r="7"/><path d="M1 8h14M8 1c3 3 3 11 0 14M8 1c-3 3-3 11 0 14" stroke="#fff" stroke-width="1" fill="none"/></svg>
        www.websitename.com
      </li>
    </ul>
  </section>
</body>
</html>
```